Travel Group 'Lydgate Group' needs a new business card design

Lydgate Group is a diverse business specialising in bespoke, tailor made holidays to suit all budgets and we are specialists in planning exciting day/short trips to suit all markets. Our target market is very varied going from the corporate client and as well as people in the community who simply want to experience something special.
We are looking for a card design that will encourage people to look at our websites and social media platforms and to see for themselves the different facets to our business. It is essential that the card has social media icons for Social profile two, Social profile one and Social profile three. We are looking for a card with a blank background with no pictures and for the front side to have the attached Lydgate logo. The card should have similar colour scheme to the attached Lydgate logo.
The card must have the following information on one side:
Maud Penrose
Business Development Manager
maudpenrose@lydgatevoyages.example
Lydgate Group, 87 Quarry Lane
Corriebank, Glenmuirshire, Scotland KA19 4TN
+44 (0)1632 730182
And then the card must have the following on the second side:
(Lydgate logo)
(social media icons)
www.lydgatevoyages.example
www.lydgateoutings.example
Target Market(s)
Our target market is very varied going from the corporate client and as well as people in the community who simply want to experience something special.
Industry/Entity Type
Business
Contact Information for Business Card
Maud Penrose
+44 (0)1632 730182
(Lydgate logo)
(social media icons)
www.lydgatevoyages.example
www.lydgateoutings.example
Requirements
Must have
- It is essential that the card has social media icons for Social profile two, Social profile one & Social profile three.
Should not have
- Should not have any images other than Lydgate logo.

```html
<!DOCTYPE html>
<html lang="en">
<head>
<meta charset="utf-8">
<title>Lydgate Group – Business Card</title>
<link rel="stylesheet" href="https://fonts.googleapis.com/css2?family=Arimo:wght@400;500&display=swap">
<style>
  :root {
    --backdrop: #1f1f21;
    --card-violet: #653f97;
    --card-plum: #9a3f95;
    --card-pink: #d33b8b;
    --ink: #ffffff;
    --ink-soft: rgba(255, 255, 255, 0.92);
  }
  * { box-sizing: border-box; margin: 0; padding: 0; }
  html, body {
    width: 1200px;
    height: 800px;
    overflow: hidden;
    background: var(--backdrop);
    font-family: "Arimo", Arial, sans-serif;
    color: var(--ink);
  }
  .sheet {
    width: 1200px;
    height: 800px;
    display: flex;
    align-items: center;
    justify-content: center;
    gap: 44px;
  }
  .card {
    width: 540px;
    height: 310px;
    border-radius: 18px;
    background: linear-gradient(120deg, var(--card-violet) 0%, var(--card-plum) 45%, var(--card-pink) 85%);
    display: flex;
    flex-direction: column;
    align-items: center;
    justify-content: center;
    text-align: center;
  }

  /* Contact side */
  .card--contact { padding-top: 6px; }
  .holder-name {
    font-size: 40px;
    font-weight: 400;
    letter-spacing: 0.5px;
    line-height: 1;
  }
  .holder-role {
    font-size: 13px;
    margin-top: 2px;
    margin-bottom: 18px;
    color: var(--ink-soft);
  }
  .contact-list { list-style: none; }
  .contact-item {
    display: flex;
    flex-direction: column;
    align-items: center;
    font-size: 14px;
    line-height: 1.3;
    color: var(--ink-soft);
    margin-bottom: 3px;
  }
  .contact-icon {
    width: 12px;
    height: 12px;
    margin: 3px 0 2px;
    fill: var(--ink);
  }

  /* Brand side */
  .brand-mark {
    display: flex;
    align-items: center;
    gap: 12px;
    margin-bottom: 16px;
  }
  .brand-dot {
    width: 20px;
    height: 20px;
    border-radius: 50%;
    background: var(--ink);
  }
  .brand-name {
    font-size: 38px;
    font-weight: 500;
    letter-spacing: 4px;
  }
  .social-row {
    display: flex;
    gap: 8px;
    margin-bottom: 10px;
  }
  .social-badge {
    width: 20px;
    height: 20px;
    border: 1.3px solid var(--ink);
    border-radius: 50%;
  }
  .web-links {
    font-size: 14px;
    color: var(--ink-soft);
  }
</style>
</head>
<body>
<main class="sheet">
  <section class="card card--contact" aria-label="Business card, contact side">
    <h1 class="holder-name">MAUD PENROSE</h1>
    <p class="holder-role">Business Development Manager</p>
    <ul class="contact-list">
      <li class="contact-item">
        <svg class="contact-icon" viewBox="0 0 12 12" aria-hidden="true"><path d="M1 2.5h10v7H1z M1 2.5l5 4 5-4" fill="none" stroke="#fff" stroke-width="1.3"/><path d="M1.5 3l4.5 3.6L10.5 3V9h-9z"/></svg>
        <span>maudpenrose@lydgatevoyages.example</span>
      </li>
      <li class="contact-item">
        <svg class="contact-icon" viewBox="0 0 12 12" aria-hidden="true"><path d="M6 0.5a3.8 3.8 0 0 0-3.8 3.8C2.2 7 6 11.5 6 11.5S9.8 7 9.8 4.3A3.8 3.8 0 0 0 6 0.5zm0 5.3a1.5 1.5 0 1 1 0-3 1.5 1.5 0 0 1 0 3z"/></svg>
        <span>Lydgate Group, 87 Quarry Lane</span>
        <span>Corriebank, Glenmuirshire, Scotland KA19 4TN</span>
      </li>
      <li class="contact-item">
        <svg class="contact-icon" viewBox="0 0 12 12" aria-hidden="true"><path d="M2.6 0.8l1.9 0.2 0.8 2.5-1.3 1c0.6 1.4 1.6 2.5 3 3.2l1-1.3 2.5 0.8 0.2 1.9c-0.5 0.9-1.5 1.3-2.5 1.1C4.6 9.5 2.4 7.3 1.7 3.8 1.4 2.6 1.8 1.4 2.6 0.8z"/></svg>
        <span>+44 (0)1632 730182</span>
      </li>
    </ul>
  </section>

  <section class="card card--brand" aria-label="Business card, brand side">
    <div class="brand-mark">
      <span class="brand-dot" aria-hidden="true"></span>
      <span class="brand-name">LYDGATE</span>
    </div>
    <div class="social-row" aria-label="Social media links">
      <span class="social-badge" role="img" aria-label="Social profile one"></span>
      <span class="social-badge" role="img" aria-label="Social profile two"></span>
      <span class="social-badge" role="img" aria-label="Social profile three"></span>
    </div>
    <p class="web-links">www.lydgatevoyages.example / www.lydgateoutings.example</p>
  </section>
</main>
</body>
</html>
```